Business Card for a Jewellery Brand

Business card for an upscale jewellery brand. Attached is the brand logo and icon and color board. I am looking for two card versions: one for the founder and one is generic. The card should be elegant and convey upscale and premium feel. I am open to both square and rectangle card shapes.

Industry/Entity Type

Jewelry

Contact Information for Business Card

Two cards: (1) Sunila Perumbadi (Founder) (2) General
(1) Sunila Perumbadi card should have Name: Sunila Perumbadi, Title: Founder Email id: sunila@quelm.com.au. Phone no: +61412555307
(2) Generic card should have Email id: info@quelm.com.au. Phone no: +61431555962

Requirements
Must have
• Workmark
• ICON
• Phone no
• Email ID
• ABN: 48917205563 (Note: ABN is Business number in Australia)
• Website: www.quelm.com.au
• Instagram: quelm_jewellery
• Facebook: @quelmjewellery
Nice to have
• Tagline

```html
<!DOCTYPE html>
<html lang="en">
<head>
<meta charset="utf-8">
<title>QUELM Business Cards</title>
<link rel="stylesheet" href="https://fonts.googleapis.com/css2?family=Roboto:wght@300;400&display=swap">
<style>
  :root {
    --backdrop: #5a5b5d;
    --card-white: #ffffff;
    --rose: #e59a97;
    --rose-back: #ea9a95;
    --blush: #f7aca0;
    --fold: #c4857f;
    --mark-rose: #e0a3a0;
    --soft-text: #fde6e2;
    --text-white: #ffffff;
  }
  * { box-sizing: border-box; margin: 0; padding: 0; }
  html, body {
    width: 1200px; height: 1200px; overflow: hidden;
    background: var(--backdrop);
    font-family: "Roboto", Arial, sans-serif;
  }
  .canvas { position: relative; width: 1200px; height: 1200px; }
  .card {
    position: absolute; left: 190px; width: 820px; height: 495px;
    overflow: hidden;
  }
  .card--front { top: 90px; background: var(--card-white); }
  .card--back { top: 615px; background: var(--rose-back); }

  .front__panel {
    position: absolute; left: 440px; top: 0; right: 0; bottom: 0;
    background: var(--rose);
  }
  .front__wordmark {
    position: absolute; left: 58px; top: 56px;
    font-size: 66px; font-weight: 400; letter-spacing: 18px;
    color: var(--mark-rose); line-height: 1;
  }
  .front__emblem {
    position: absolute; left: 62px; top: 180px;
    width: 230px; height: 230px; border-radius: 50%;
    border: 14px solid var(--mark-rose);
  }
  .name-band {
    position: absolute; left: 405px; top: 48px; width: 415px; height: 82px;
    background: var(--blush); padding: 14px 0 0 62px;
  }
  .name-band__fold {
    position: absolute; left: 405px; top: 130px; width: 35px; height: 32px;
  }
  .name-band__name { font-size: 31px; font-weight: 300; color: var(--text-white); line-height: 1.1; }
  .name-band__title { font-size: 21px; font-weight: 400; color: var(--soft-text); margin-top: 4px; }

  .address {
    position: absolute; left: 475px; top: 188px;
    font-size: 23px; line-height: 31px; color: var(--text-white); font-style: normal;
  }
  .contacts {
    position: absolute; left: 475px; top: 268px; list-style: none;
    font-size: 23px; line-height: 32px; color: var(--text-white);
  }
  .contacts li { display: flex; align-items: center; gap: 7px; }
  .contacts svg { width: 17px; height: 17px; flex: none; }
  .social-square { width: 15px; height: 15px; background: var(--text-white); flex: none; margin: 0 1px; }

  .abn-band {
    position: absolute; left: 25px; top: 432px; width: 435px; height: 40px;
    background: var(--blush); padding-left: 52px;
    font-size: 22px; line-height: 40px; color: var(--text-white);
  }

  .back__brand {
    position: absolute; inset: 0;
    display: flex; flex-direction: column; align-items: center; justify-content: center;
    gap: 34px;
  }
  .back__circle {
    width: 90px; height: 90px; border: 6px solid var(--text-white); border-radius: 50%;
  }
  .back__wordmark {
    font-size: 86px; font-weight: 400; letter-spacing: 30px; margin-right: -30px;
    color: var(--text-white); line-height: 1;
  }
</style>
</head>
<body>
<main class="canvas">
  <section class="card card--front" aria-label="Founder card, front">
    <div class="front__panel"></div>
    <div class="front__wordmark">QUELM</div>
    <div class="front__emblem" aria-hidden="true"></div>

    <svg class="name-band__fold" viewBox="0 0 35 32" aria-hidden="true">
      <polygon points="0,0 35,0 35,32" fill="var(--fold)"/>
    </svg>
    <div class="name-band">
      <p class="name-band__name">Sunila Perumbadi</p>
      <p class="name-band__title">Founder</p>
    </div>

    <address class="address">
      742 Harlow Street, Suite 3100<br>
      Fairbrook, Maryland 20911
    </address>

    <ul class="contacts">
      <li>
        <svg viewBox="0 0 24 24" aria-hidden="true"><path fill="#fff" d="M6.6 10.8a15 15 0 0 0 6.6 6.6l2.2-2.2c.3-.3.7-.4 1-.2 1.1.4 2.3.6 3.6.6.6 0 1 .4 1 1V20c0 .6-.4 1-1 1A17 17 0 0 1 3 4c0-.6.4-1 1-1h3.5c.6 0 1 .4 1 1 0 1.3.2 2.5.6 3.6.1.3 0 .7-.2 1z"/></svg>
        +61412555307
      </li>
      <li>
        <svg viewBox="0 0 24 24" aria-hidden="true"><rect x="2" y="5" width="20" height="14" fill="#fff"/><path d="M2 5l10 8 10-8" fill="none" stroke="var(--rose)" stroke-width="2"/></svg>
        sunila@quelm.com.au
      </li>
      <li>
        <svg viewBox="0 0 24 24" aria-hidden="true"><g fill="none" stroke="#fff" stroke-width="2"><circle cx="12" cy="12" r="9"/><ellipse cx="12" cy="12" rx="4" ry="9"/><path d="M3 12h18"/></g></svg>
        www.quelm.com.au
      </li>
      <li><span class="social-square" aria-hidden="true"></span>quelm_jewellery</li>
      <li><span class="social-square" aria-hidden="true"></span>@quelmjewellery</li>
    </ul>

    <div class="abn-band">ABN: 48917205563</div>
  </section>

  <section class="card card--back" aria-label="Card back">
    <div class="back__brand">
      <div class="back__circle" aria-hidden="true"></div>
      <div class="back__wordmark">QUELM</div>
    </div>
  </section>
</main>
</body>
</html>
```